Refer a Friend A5 Flyer for Healthcare Staff

We need an A5 flyer that we can hand out to existing and new staff members promoting our Refer a friend Scheme. We need the leaflet to encourage staff to talk to their family and friends about joining our Healthcare Agency, which provides staff to local care related establishments. Using our logo and brand colours blue and green, as per our website, the final design will need to clearly convey the benefits and attractions of referring additional staff to the team. In addition is the promotion of our Socialsphere page, requesting staff to like the page and to like and share various posts.

Target Market(s)

Healthcare and potential Healthcare Staff

Industry/Entity Type

Healthcare

Colors
33b8a4
3277b5

Requirements
Must have
• Company Logo, Brand colours,
• text; "Refer a Friend and receive a £50 Bonus after just 1 completed shift"
• text; "3 easy steps to refer a friend, 1 Fill out your name on the back of your Business Card 2 Hand the card to your friend or any person you wish to refer, 3 ask your friend to present the card to us when they attend their interview"
• text; "Like and share any of our Open Days on Socialsphere for a chance to win a prize, you can find us easily by searching @CarewellPlacementGroup"
• text; "Like our Page to stay up to date with our events and offers"
Nice to have
• care worker / elderly care / support worker pictures
• Content / pics from website www.carewellplacementgroup.co.uk

```html
<!DOCTYPE html>
<html lang="en">
<head>
<meta charset="utf-8">
<title>Carewell Placement – Refer a Friend Flyer</title>
<link href="https://fonts.googleapis.com/css2?family=Oswald:wght@500;600&family=Montserrat:wght@300;400;500&display=swap" rel="stylesheet">
<style>
  :root {
    --brand-green: #33b8a4;
    --band-green: #2db09b;
    --brand-blue: #3277b5;
    --ink: #3a3a3a;
    --paper: #ffffff;
    --scrubs-light: #dfe9f3;
    --scrubs-mid: #b9cde2;
  }
  * { margin: 0; padding: 0; box-sizing: border-box; }
  html, body { width: 1200px; height: 789px; overflow: hidden; background: var(--paper); }
  .flyer {
    position: relative;
    width: 1200px;
    height: 789px;
    background: var(--paper);
    font-family: "Montserrat", sans-serif;
    color: var(--ink);
  }
  .brand {
    position: absolute;
    left: 60px;
    top: 62px;
    display: flex;
    align-items: center;
    gap: 14px;
  }
  .brand-mark {
    width: 26px;
    height: 26px;
    border-radius: 50%;
    background: var(--brand-green);
  }
  .brand-name {
    font-family: "Oswald", sans-serif;
    font-weight: 500;
    font-size: 36px;
    line-height: 1;
    color: var(--brand-blue);
    letter-spacing: 0.5px;
  }
  .headline {
    position: absolute;
    left: 470px;
    top: 58px;
    font-family: "Oswald", sans-serif;
    font-weight: 600;
    font-size: 40px;
    line-height: 42px;
    text-transform: uppercase;
    color: var(--brand-blue);
  }
  .headline .accent { color: var(--brand-green); }
  .steps-band {
    position: absolute;
    left: 0;
    top: 196px;
    width: 760px;
    height: 360px;
    background: var(--band-green);
    padding: 34px 0 0 60px;
    color: var(--paper);
  }
  .steps-title {
    font-family: "Oswald", sans-serif;
    font-weight: 500;
    font-size: 32px;
    text-transform: uppercase;
    letter-spacing: 0.3px;
    margin-bottom: 22px;
  }
  .step-list { list-style: none; position: relative; }
  .step-list::before {
    content: "";
    position: absolute;
    left: 38px;
    top: 30px;
    bottom: 40px;
    width: 3px;
    background: var(--paper);
  }
  .step {
    position: relative;
    display: flex;
    align-items: flex-start;
    gap: 30px;
    height: 82px;
  }
  .step-number {
    flex: none;
    width: 78px;
    height: 78px;
    border-radius: 50%;
    background: var(--paper);
    color: var(--band-green);
    font-family: "Oswald", sans-serif;
    font-weight: 500;
    font-size: 36px;
    display: flex;
    align-items: center;
    justify-content: center;
    position: relative;
    z-index: 1;
    transform: scale(0.9);
  }
  .step-text {
    font-weight: 300;
    font-size: 20px;
    line-height: 24px;
    padding-top: 10px;
    max-width: 380px;
  }
  .team-photo {
    position: absolute;
    left: 640px;
    top: 240px;
    width: 520px;
    height: 530px;
    background: radial-gradient(ellipse at 50% 45%, var(--scrubs-light) 0%, var(--scrubs-mid) 55%, rgba(185,205,226,0) 72%);
  }
  .social {
    position: absolute;
    left: 60px;
    top: 600px;
    display: flex;
    gap: 20px;
    align-items: flex-start;
    width: 600px;
  }
  .social-badge {
    flex: none;
    width: 62px;
    height: 56px;
    background: var(--brand-blue);
  }
  .social-text {
    font-size: 15.5px;
    line-height: 22px;
    font-weight: 400;
    color: var(--ink);
  }
  .social-text .link { color: var(--brand-blue); }
</style>
</head>
<body>
  <main class="flyer">
    <div class="brand">
      <span class="brand-mark"></span>
      <span class="brand-name">Carewell Placement</span>
    </div>

    <h1 class="headline">
      <span class="accent">Refer a friend</span> and receive a <span class="accent">£50 bonus</span><br>
      after just 1 completed shift
    </h1>

    <section class="steps-band">
      <h2 class="steps-title">3 easy steps to refer a friend</h2>
      <ol class="step-list">
        <li class="step"><span class="step-number">1</span><p class="step-text">Fill out your name on the back of your Business Card</p></li>
        <li class="step"><span class="step-number">2</span><p class="step-text">Hand the card to your friend or any person you wish to refer</p></li>
        <li class="step"><span class="step-number">3</span><p class="step-text">Ask your friend to present the card to us when they attend their interview</p></li>
      </ol>
    </section>

    <div class="team-photo" role="img" aria-label="Photo of a team of healthcare staff in light blue scrubs joining hands in the middle"></div>

    <footer class="social">
      <span class="social-badge"></span>
      <p class="social-text">
        Like and share any of our <span class="link">Open Days</span> on Socialsphere for a chance to win a prize, you can find us easily by searching
        <span class="link">@CarewellPlacementGroup</span> Like our Page to stay up to date with our events and offers
      </p>
    </footer>
  </main>
</body>
</html>
```